Harbor Vantage Business Card

I need a business card for my firearm business. On one side I want the Harbor Vantage skull logo with the writing (tag on LLC at the end of Harbor Vantage). I want it to be dark, sharp, and look professional. I would like a small American flag in the corner of the card also. The other side of the card is where I want all the info. The info I want on the card will be my contact info as well as what kind of business it is. The contact info is:
Dana Whitlow
Founder and Owner
d.whitlow@harborvantage-example.com
555-304-7718
I want the Harbor Vantage logo with just the skull on this side also.The info I want about the business is:
- Class Three Dealer
- Certified Gunsmith/Armorer
- Certified Firearm Instructor
If you can give the background a gothic but professional feel that would be great! Hope we can work together on this and I look forward to hearing from you soon. Thank you!
Target Market(s)
Firearms, guns, training, gunsmithing
Industry/Entity Type
Gun
Contact Information for Business Card
Dana Whitlow
Founder and Owner
555-304-7718
- Class Three Dealer

```html
<!DOCTYPE html>
<html lang="en">
<head>
<meta charset="utf-8">
<title>Harbor Vantage – Business Card</title>
<link href="https://fonts.googleapis.com/css2?family=Archivo+Black&family=Lato:wght@400;700;900&display=swap" rel="stylesheet">
<style>
  :root {
    --card-black: #000000;
    --panel-grey: #8f9e9c;
    --box-black: #19191b;
    --ink-dark: #1b1b1b;
    --ink-light: #ffffff;
    --ink-grey: #98a5a3;
    --crop-red: #c0272d;
  }
  html, body {
    margin: 0;
    padding: 0;
    width: 1200px;
    height: 702px;
    overflow: hidden;
    background: var(--card-black);
  }
  .card {
    position: relative;
    width: 1200px;
    height: 702px;
    background: var(--card-black);
    font-family: "Lato", sans-serif;
  }
  .card-shapes {
    position: absolute;
    inset: 0;
  }
  .crop-mark {
    position: absolute;
    width: 14px;
    height: 14px;
    border-color: var(--crop-red);
    border-style: solid;
    border-width: 0;
  }
  .crop-mark.top-left { left: 8px; top: 8px; border-right-width: 2px; border-bottom-width: 2px; }
  .crop-mark.bottom-left { left: 8px; bottom: 8px; border-right-width: 2px; border-top-width: 2px; }
  .crop-mark.bottom-right { right: 8px; bottom: 8px; border-left-width: 2px; border-top-width: 2px; }

  .brand {
    position: absolute;
    left: 250px;
    top: 190px;
    width: 680px;
    display: flex;
    align-items: center;
    justify-content: center;
    gap: 18px;
  }
  .brand-mark {
    width: 30px;
    height: 30px;
    background: var(--ink-dark);
  }
  .brand-name {
    margin: 0;
    font-family: "Lato", sans-serif;
    font-weight: 900;
    font-size: 42px;
    letter-spacing: 3px;
    text-transform: uppercase;
    color: var(--ink-dark);
  }
  .person-name {
    position: absolute;
    left: 93px;
    top: 296px;
    margin: 0;
    font-family: "Archivo Black", sans-serif;
    font-size: 54px;
    line-height: 1;
    color: var(--ink-dark);
  }
  .person-role {
    position: absolute;
    left: 97px;
    top: 386px;
    margin: 0;
    font-family: "Lato", sans-serif;
    font-weight: 900;
    font-size: 27px;
    letter-spacing: 2px;
    color: var(--ink-dark);
  }
  .phone {
    position: absolute;
    left: 97px;
    top: 480px;
    margin: 0;
    font-size: 40px;
    line-height: 1;
    color: var(--ink-light);
  }
  .services {
    position: absolute;
    right: 88px;
    top: 384px;
    margin: 0;
    padding: 0;
    list-style: none;
    text-align: right;
    font-size: 33px;
    line-height: 50px;
    color: var(--ink-grey);
  }
  .email {
    position: absolute;
    left: 95px;
    top: 560px;
    margin: 0;
    font-size: 36px;
    line-height: 1;
    letter-spacing: 6px;
    color: var(--ink-dark);
  }
</style>
</head>
<body>
  <div class="card">
    <svg class="card-shapes" width="1200" height="702" viewBox="0 0 1200 702" aria-hidden="false">
      <defs>
        <linearGradient id="flag-tones" x1="0" y1="0" x2="1" y2="1">
          <stop offset="0" stop-color="#1a1a1a"/>
          <stop offset="0.55" stop-color="#2a2d2d"/>
          <stop offset="1" stop-color="#6d7877"/>
        </linearGradient>
      </defs>
      <!-- upper grey panel with angled corner -->
      <polygon class="top-panel" points="81,74 930,74 1123,250 1123,368 81,368" fill="var(--panel-grey)"/>
      <!-- corner flag area -->
      <polygon class="corner-flag" role="img" aria-label="Small American flag with stars and curved stripes in the corner"
               points="930,74 1168,0 1200,0 1200,300 1123,250" fill="url(#flag-tones)"/>
      <!-- divider line -->
      <rect class="divider" x="81" y="368" width="1042" height="6" fill="var(--card-black)"/>
      <!-- role box -->
      <rect class="role-box" x="81" y="374" width="565" height="169" fill="var(--panel-grey)"/>
      <!-- phone box -->
      <rect class="phone-box" x="81" y="462" width="384" height="81" fill="var(--box-black)"/>
      <!-- services box -->
      <rect class="services-box" x="646" y="374" width="479" height="169" fill="var(--box-black)"/>
      <!-- email bar -->
      <rect class="email-bar" x="81" y="550" width="1042" height="66" fill="var(--panel-grey)"/>
    </svg>

    <span class="crop-mark top-left"></span>
    <span class="crop-mark bottom-left"></span>
    <span class="crop-mark bottom-right"></span>

    <div class="brand">
      <span class="brand-mark"></span>
      <h1 class="brand-name">Harbor Vantage LLC</h1>
    </div>

    <h2 class="person-name">Dana Whitlow</h2>
    <p class="person-role">Founder and Owner</p>
    <p class="phone">P: 555-304-7718</p>

    <ul class="services">
      <li>Class Three Dealer</li>
      <li>Gunsmith/Armorer</li>
      <li>Certified Firearm Instructor</li>
    </ul>

    <p class="email">E:d.whitlow@harborvantage-example.com</p>
  </div>
</body>
</html>
```